Create a new business card

I’m looking to update my business card to make it match the rest of my brand. I will include my current website as well as what my vehicle designs look like, etc..
What my business currently services
Weekly maintenance pool openings / closings
Equipment repair, including pumps, heaters, salt systems, filters, etc.
We install automatic covers and maintain them as well as provide preventative maintenance

I would like to include my name.
Bradley Kessner.
My title
Owner
My email
Brad@wavecrewnx.com
5079164826
Www.wavecrewnx.com

```html
<!DOCTYPE html>
<html lang="en">
<head>
<meta charset="utf-8">
<title>Business Card – Bradley Kessner</title>
<link href="https://fonts.googleapis.com/css2?family=Roboto:wght@400;700&display=swap" rel="stylesheet">
<style>
  :root {
    --page-bg: #d9d6d1;
    --card-bg: #eef0f1;
    --card-edge: #c9cdd1;
    --navy: #1f2a4d;
    --accent-red: #c8412b;
    --text-grey: #3a3f4a;
    --icon-blue: #2a7fb8;
    --emblem-fill: #d6e8f3;
    --emblem-ring: #2a8cc4;
  }
  * { margin: 0; padding: 0; box-sizing: border-box; }
  html, body {
    width: 1200px;
    height: 969px;
    overflow: hidden;
    background: var(--page-bg);
    font-family: "Roboto", Arial, sans-serif;
  }
  .card {
    position: absolute;
    left: 80px;
    top: 187px;
    width: 1040px;
    height: 594px;
    background: var(--card-bg);
    border: 2px solid var(--card-edge);
    border-radius: 28px;
    overflow: hidden;
  }
  .contact-block {
    position: absolute;
    left: 72px;
    top: 300px;
  }
  .person-name {
    font-weight: 700;
    font-size: 32px;
    color: var(--navy);
    line-height: 1.1;
  }
  .person-title {
    font-weight: 700;
    font-size: 23px;
    color: var(--accent-red);
    margin-top: 4px;
  }
  .contact-list {
    list-style: none;
    margin-top: 52px;
  }
  .contact-item {
    display: flex;
    align-items: center;
    gap: 14px;
    font-size: 25px;
    color: var(--text-grey);
    height: 33px;
  }
  .contact-icon {
    width: 22px;
    height: 22px;
    flex: none;
    fill: var(--icon-blue);
  }
  .brand-mark {
    position: absolute;
    left: 438px;
    top: 14px;
    width: 566px;
    height: 566px;
    display: flex;
    align-items: center;
    justify-content: center;
  }
  .brand-circle {
    position: absolute;
    inset: 0;
    border-radius: 50%;
    background: var(--emblem-fill);
    border: 14px solid var(--emblem-ring);
  }
  .brand-name {
    position: relative;
    font-weight: 700;
    font-size: 78px;
    line-height: 1.12;
    color: var(--navy);
    text-align: center;
  }
</style>
</head>
<body>
  <div class="card">
    <div class="contact-block">
      <p class="person-name">Bradley Kessner</p>
      <p class="person-title">Owner</p>
      <ul class="contact-list">
        <li class="contact-item">
          <svg class="contact-icon" viewBox="0 0 24 24" aria-hidden="true"><path d="M6.6 10.8a15.1 15.1 0 0 0 6.6 6.6l2.2-2.2c.3-.3.7-.4 1-.2 1.1.4 2.3.6 3.6.6.6 0 1 .4 1 1V20c0 .6-.4 1-1 1A17 17 0 0 1 3 4c0-.6.4-1 1-1h3.5c.6 0 1 .4 1 1 0 1.3.2 2.5.6 3.6.1.3 0 .7-.2 1z"/></svg>
          <span>5079164826</span>
        </li>
        <li class="contact-item">
          <svg class="contact-icon" viewBox="0 0 24 24" aria-hidden="true"><path d="M2 5h20v14H2z" opacity=".9"/><path d="M2 5l10 8 10-8" fill="none" stroke="#eef0f1" stroke-width="2"/></svg>
          <span>Brad@wavecrewnx.com</span>
        </li>
        <li class="contact-item">
          <svg class="contact-icon" viewBox="0 0 24 24" aria-hidden="true"><circle cx="12" cy="12" r="10"/><path d="M7 8c2 0 3 1 3 3s-2 2-2 4M14 5c0 2 2 3 4 3M15 19c0-2 1-3 3-3" fill="none" stroke="#eef0f1" stroke-width="1.6"/></svg>
          <span>www.wavecrewnx.com</span>
        </li>
      </ul>
    </div>

    <div class="brand-mark">
      <div class="brand-circle"></div>
      <p class="brand-name">Wave Crew<br>Pool<br>Service</p>
    </div>
  </div>
</body>
</html>
```